Thorvane Leadership Flyer - Redesign

Thorvane Consulting is looking to update and redesign our one page leave behind. This page is part of the package left with prospective clients after meetings. It explains what Thorvane does. Recently, we used pixel forum to create a new logo for our new business name "Thorvane Leadership". We would like this new logo to replace the current "Thorvane Consulting" logo. We are looking for this re-designed piece to be easy to read, clean and professional, updating the design, including the graphics and layout. We typically use shades of blue (as in the Thorvane Leaderhip logo - attached).

Target Market(s)

Prospective clients

Industry/Entity Type

Management Consulting

Font styles to use
Serif
Sans Serif

Colors
3176b5
33a6d7
85cae6
0255a3
3276b5
85abd2
cfdeed
cee9f5

Requirements
Must have
• New Thorvane Leadership logo in place of the Thorvane Consulting logo.
• Professional design.
• Formatted so that simple copy changes can be easily made, as necessary.
Should not have
• More than one page

```html
<!DOCTYPE html>
<html lang="en">
<head>
<meta charset="utf-8">
<title>Thorvane Leadership – Leave-Behind Flyer</title>
<link rel="stylesheet" href="https://fonts.googleapis.com/css2?family=Lato:wght@400;700&display=swap">
<style>
  :root{
    --navy:#0255a3;
    --brand-blue:#3276b5;
    --sky:#85cae6;
    --sky-pale:#cee9f5;
    --steel:#1f4d5f;
    --ink:#222831;
    --logo-ink:#1d4f7c;
    --paper:#ffffff;
    --backdrop:#eceef1;
  }
  *{box-sizing:border-box;margin:0;padding:0}
  html,body{width:900px;height:1200px;overflow:hidden;background:var(--backdrop)}
  body{font-family:"Lato",Arial,sans-serif;color:var(--ink)}
  .canvas{position:relative;width:900px;height:1200px;overflow:hidden}
  .flyer{
    position:absolute;left:30px;top:60px;width:720px;height:925px;
    transform:scale(1.1667);transform-origin:0 0;
    background:var(--paper);overflow:hidden;
    box-shadow:0 2px 6px rgba(0,0,0,.15);
  }
  .flyer-shapes{position:absolute;inset:0;width:720px;height:925px}
  .brand{
    position:absolute;left:0;right:0;top:40px;
    display:flex;align-items:center;justify-content:center;gap:14px;
  }
  .brand-dot{width:22px;height:22px;border-radius:50%;background:var(--logo-ink)}
  .brand-name{font-size:36px;font-weight:700;color:var(--logo-ink);letter-spacing:.5px}
  .headline{
    position:absolute;left:38px;top:478px;color:#fff;font-weight:700;line-height:1.22;
  }
  .headline .big{font-size:36px;display:block}
  .headline .small{font-size:25px;display:block;margin-top:2px}
  .tab-label{position:absolute;color:#fff;font-weight:700;font-size:30px}
  .tab-about{left:563px;top:495px}
  .tab-services{left:24px;top:627px}
  .body-copy{position:absolute;font-size:13.6px;line-height:18px;text-align:justify;hyphens:auto}
  .body-copy p{margin:0}
  .about-copy{left:390px;top:576px;width:308px;text-align-last:right}
  .services-copy{left:23px;top:688px;width:322px}
  .phone{
    position:absolute;left:420px;top:758px;display:flex;align-items:center;gap:12px;
    color:#fff;font-weight:700;font-size:31px;
  }
  .phone svg{width:24px;height:24px}
  .footer-contact{position:absolute;left:0;right:0;top:834px;text-align:center;color:#fff}
  .footer-contact .addr{font-size:16px;line-height:20px}
  .footer-contact .addr svg{width:18px;height:16px;vertical-align:-2px;margin-right:4px}
  .footer-contact .email{font-size:22px;font-weight:700;margin-top:10px}
  .footer-contact .email svg{width:20px;height:20px;vertical-align:-3px;margin-right:6px}
</style>
</head>
<body>
<main class="canvas">
  <article class="flyer">
    <svg class="flyer-shapes" viewBox="0 0 720 925" xmlns="http://www.w3.org/2000/svg">
      <defs>
        <linearGradient id="photoTone" x1="0" y1="0" x2="1" y2="1">
          <stop offset="0" stop-color="#d9dee4"/>
          <stop offset=".45" stop-color="#8f98a3"/>
          <stop offset="1" stop-color="#e7ecf1"/>
        </linearGradient>
        <linearGradient id="contentTone" x1="0" y1="0" x2="0" y2="1">
          <stop offset="0" stop-color="#f5f6f8"/>
          <stop offset="1" stop-color="#e4e7eb"/>
        </linearGradient>
      </defs>

      <rect class="meeting-photo" x="0" y="90" width="720" height="390" fill="url(#photoTone)"
            role="img" aria-label="Photograph of two consultants reviewing documents at a meeting table in a bright office"/>

      <!-- header wave -->
      <path d="M0 0H720V95C520 150 250 160 0 105Z" fill="var(--paper)"/>
      <path d="M0 105C250 160 520 150 720 95V125C520 172 250 178 0 132Z" fill="var(--sky)"/>
      <path d="M0 105C250 160 520 150 720 95" fill="none" stroke="var(--navy)" stroke-width="7"/>

      <!-- content area with lower photo wave -->
      <path d="M0 470C250 445 500 435 720 460V925H0Z" fill="url(#contentTone)"/>
      <path d="M0 440C250 395 500 392 720 405V462C500 437 250 447 0 472Z" fill="var(--sky)"/>
      <path d="M0 440C250 395 500 392 720 405V396C500 381 250 384 0 428Z" fill="var(--navy)"/>

      <!-- headline box -->
      <path d="M26 461H334V593Q334 607 320 607H40Q26 607 26 593Z" fill="#24588d"/>
      <path d="M20 455H328V589Q328 603 314 603H34Q20 603 20 589Z" fill="var(--brand-blue)"/>

      <!-- about us tab -->
      <path d="M502 514L568 469V492H720V538H568V560Z" fill="var(--steel)"/>

      <!-- our services tab -->
      <path d="M0 620H150V602L223 646L150 691V672H0Z" fill="var(--steel)"/>

      <!-- phone pill -->
      <path d="M427 752H720V806H427A27 27 0 0 1 427 752Z" fill="var(--brand-blue)"/>

      <!-- footer -->
      <path d="M0 886Q360 730 720 886" fill="none" stroke="#b9bec5" stroke-width="8"/>
      <path d="M0 895Q360 745 720 895V925H0Z" fill="var(--brand-blue)"/>
    </svg>

    <header class="brand">
      <span class="brand-dot"></span>
      <span class="brand-name">Thorvane Leadership</span>
    </header>

    <h1 class="headline">
      <span class="big">Leadership &amp;</span>
      <span class="big">Management</span>
      <span class="small">Solutions for Business</span>
    </h1>

    <h2 class="tab-label tab-about">About Us</h2>
    <section class="body-copy about-copy">
      <p>Based in the Gulf South region of the United States, Thorvane Management Consulting provides its Leadership and management consulting services to a national arena via this web site. No matter where you're located in the U.S., we bring the knowledge and expertise of Leadership to you. Contact us today for information on how we can make the experience not only the best solution, but the most convenient.</p>
    </section>

    <div class="phone">
      <svg viewBox="0 0 24 24" aria-hidden="true"><path fill="#fff" d="M6.6 10.8a15.1 15.1 0 0 0 6.6 6.6l2.2-2.2c.3-.3.7-.4 1-.2 1.1.4 2.3.6 3.6.6.6 0 1 .4 1 1V20c0 .6-.4 1-1 1A17 17 0 0 1 3 4c0-.6.4-1 1-1h3.5c.6 0 1 .4 1 1 0 1.3.2 2.5.6 3.6.1.3 0 .7-.2 1Z"/></svg>
      <span>(504) 555-0148</span>
    </div>

    <h2 class="tab-label tab-services">Our Services</h2>
    <section class="body-copy services-copy">
      <p>Thorvane Management Consulting provides Leadership and Management consulting and implementation services to business.</p>
      <p>Thorvane Management Consulting tailors its problem-solving approach to each client's needs. We understand every client's situation is unique. In-depth, closely coordinated work with clients is our approach.</p>
    </section>

    <footer class="footer-contact">
      <div class="addr"><svg viewBox="0 0 18 16" aria-hidden="true"><path fill="#fff" d="M9 0L0 8h2.5v8h4.5v-5h4v5h4.5V8H18Z"/></svg>1407 Larkmoor Ave.</div>
      <div class="addr">New Orleans, LA 70119</div>
      <div class="email"><svg viewBox="0 0 20 20" aria-hidden="true"><g fill="none" stroke="#fff" stroke-width="1.6"><circle cx="10" cy="10" r="8.5"/><ellipse cx="10" cy="10" rx="3.8" ry="8.5"/><path d="M1.5 10h17M3 5.5h14M3 14.5h14"/></g></svg>consult@thorvaneconsulting.com</div>
    </footer>
  </article>
</main>
</body>
</html>
```